Web Site Design for new Children's Book Series

We need a new web site design that complements a new children's book series that will be available next month. The main character is named 'Pimble Wocket Otter Cat Fish' and the story lines work through bullying issues for elementary age kids. This is a new design from scratch, but we have attached a collection of artwork from the new book series that the web site design should complement.

The scope of this project is only for the design / layout of the home page and one interior page for the web site.

Additional project details including the sitemap and example content are included in the attached document: 'Pimble Wocket Web Site.pdf'

We are open for questions and we look forward to seeing your creativity!

We have marked the project as guaranteed now!  We look forward to seeing your ideas and concepts!

Target Market(s)

Currently, there are two children’s books in the Pimble Wocket series aimed at elementary aged children. This collection is planned to grow over time. The goal of the web site is to provide information about the authors and the book series to elementary aged children (ages 3 to 12), their parents, and their school teachers and counselors.

Industry/Entity Type

Interior

Requirements
Must have
• The web site design should complement the attached artwork from the Pimble Wocket series. Overall, a full width design is desired that utilizes and open layout with lots of color.

The Pimble Wocket animal logo should be prominently placed. It is not necessary to retain the white background behind the logo.

The web site will be implemented as a responsive design using the Twitter Bootstrap framework and a standard 12 column grid.
Nice to have
• There are two themes in the books which should be incorporated into the web site design:

- Pimble Wocket uses the phrase “Way Cool” in describing various characters in the book and it is meant to build confidence and self esteem ... "you are way cool"

- An eagle feather is left behind as in “Wocket was here”. This eagle feature should be incorporated into the design in various locations.

```html
<!DOCTYPE html>
<html lang="en">
<head>
<meta charset="utf-8">
<title>Pimble Wocket – Home</title>
<link rel="stylesheet" href="https://fonts.googleapis.com/css2?family=Advent+Pro:wght@300;400&display=swap">
<style>
  :root{
    --white:#ffffff;
    --ink:#1a1a1a;
    --sage:#8fae9b;
    --clay:#d18e72;
    --violet:#8472b8;
    --rose:#c0628a;
    --moss:#7e9656;
    --sky:#7594d0;
    --peach:#fcc58b;
    --feather:#0b0b0b;
  }
  *{margin:0;padding:0;box-sizing:border-box}
  html,body{width:1131px;height:1200px;overflow:hidden;background:var(--white)}
  body{position:relative;font-family:"Advent Pro",sans-serif;color:var(--ink);font-weight:400}
  a{color:var(--white);text-decoration:none}

  .main-nav{position:absolute;top:0;left:0;width:1131px;height:74px}
  .main-nav ul{list-style:none;display:flex;justify-content:space-between;position:absolute;left:86px;top:17px;width:952px;height:57px}
  .main-nav li{font-size:23px;padding:4px 6px 0;white-space:nowrap}
  .main-nav li.is-active{background:var(--sage)}
  .main-nav a{color:var(--ink)}

  .band{position:absolute;left:0;width:1131px;height:237px}
  .intro{top:74px;background:var(--sage);height:238px}
  .release{top:329px;background:var(--clay)}
  .row-top{top:584px}
  .row-bottom{top:838px}
  .half-left,.half-right{position:absolute;top:0;height:100%}
  .half-left{left:0;width:567px}
  .half-right{left:567px;width:564px}
  .row-top .half-left{background:var(--violet)}
  .row-top .half-right{background:var(--rose)}
  .row-bottom .half-left{background:var(--moss)}
  .row-bottom .half-right{background:var(--sky)}

  .art{position:absolute}
  .art-mascot{left:91px;top:0;width:163px;height:238px;border-radius:40px 40px 8px 8px;
    background:linear-gradient(160deg,#f1efe6 0%,#8a4a24 40%,#2b1d14 75%,#d9a321 100%)}
  .art-cover{left:856px;top:0;width:180px;height:237px;
    background:linear-gradient(180deg,#e7753e 0%,#2f5a2f 22%,#3c3c3c 55%,#6fb9b0 85%,#4cb8c0 100%)}
  .art-feather{left:510px;top:584px;width:110px;height:491px;border-radius:55px 55px 30px 30px;
    background:linear-gradient(180deg,var(--feather),#1e1e1e)}

  h2{font-weight:400;font-size:24px;white-space:nowrap}
  .centered{text-align:center}
  .intro-copy{position:absolute;left:370px;top:44px;width:640px;font-size:17px;line-height:24.5px}
  .release-copy{position:absolute;left:122px;top:44px;width:668px;font-size:17px;line-height:24.5px}

  .blog-list{position:absolute;left:91px;top:34px;font-size:17px;line-height:24.5px}
  .blog-list ul{list-style:none}
  .blog-list li{white-space:nowrap}
  .blog-list a{margin-left:10px}

  .signup{position:absolute;right:93px;top:34px;width:440px;text-align:right}
  .signup h2{margin-bottom:6px}
  .signup .field{display:block;width:289px;height:31px;margin:0 0 9px auto;background:var(--white);
    font-size:17px;text-align:left;padding:4px 10px;color:var(--ink)}
  .signup .submit{display:inline-block;width:143px;height:31px;background:var(--white);
    font-size:18px;text-align:center;padding-top:3px}

  .visits{position:absolute;left:93px;top:43px;font-size:17px;line-height:24.5px}

  .readers{position:absolute;left:147px;top:30px;width:324px;font-size:13px;line-height:18px}
  .readers h2{text-align:center;margin-bottom:4px}
  .readers cite{display:block;text-align:right;font-style:normal;color:var(--white);margin:0 10px 4px 0}

  .site-footer{position:absolute;left:0;top:1094px;width:1131px;height:70px;background:var(--peach);
    text-align:center;font-size:24px;padding-top:20px}
</style>
</head>
<body>
  <nav class="main-nav">
    <ul>
      <li class="is-active"><a href="#">Home</a></li>
      <li><a href="#">About the Authors</a></li>
      <li><a href="#">The Books</a></li>
      <li><a href="#">Schedule a Visit</a></li>
      <li><a href="#">Glow and Grow</a></li>
      <li><a href="#">Teachable Moments</a></li>
      <li><a href="#">Contact Us</a></li>
      <li><a href="#">Blog</a></li>
    </ul>
  </nav>

  <section class="band intro">
    <div class="art art-mascot" role="img" aria-label="Pimble Wocket mascot illustration"></div>
    <div class="intro-copy centered">
      <h2>Introducing Pimble Wocket</h2>
      <p>Pimble, the hound dog and Wocket, the eagle, lived along the Tansy River in Wrenfield, Brook County. While playing one day, they became an unusual character named Pimble Wocket Otter Cat Fish. Pimble and Wocket travel throughout the book adjusting to their new body and learning how to use their "super powers" for good. They help kids learn how to feel good about themselves, deal with bullying, and forgiveness. A must read for young children.</p>
    </div>
  </section>

  <section class="band release">
    <div class="release-copy centered">
      <h2>New Release</h2>
      <p>When the dust finally settled, Pimble and Wocket were lying on the ground, knocked out. But wait -- there was something very different about them. The two of them were in one body! The front legs were Pimble’s, and the rear legs were Wocket’s. It was a hound dog body with fur, feathers and large wings. There were two heads on the one body. One was Pimble’s with his floppy, hound dog-ears and hound dog nose; the other was Wocket’s with his white eagle feathers and yellow beak.</p>
    </div>
    <div class="art art-cover" role="img" aria-label="Book cover illustration for Pimble Wocket Otter Cat Fish"></div>
  </section>

  <section class="band row-top">
    <div class="half-left">
      <div class="blog-list">
        <h2>Blog Posts</h2>
        <ul>
          <li>Have you heared the news abou... <a href="#">read more</a></li>
          <li>The otter cat fish is on the move... <a href="#">read more</a></li>
          <li>...and he said - Way Cool !... <a href="#">read more</a></li>
          <li>- I thought I heared something Wocket... <a href="#">read more</a></li>
          <li>We are going in circles you know.<a href="#" style="margin-left:2px">read more</a></li>
          <li>That’s more like it!... <a href="#">read more</a></li>
        </ul>
      </div>
    </div>
    <div class="half-right">
      <form class="signup">
        <h2>Get updates and news from Pimble and Wocket</h2>
        <span class="field">Your name...</span>
        <span class="field">Your email...</span>
        <span class="submit">Keep me updated!</span>
      </form>
    </div>
  </section>

  <section class="band row-bottom">
    <div class="half-left">
      <div class="visits">
        <h2>Author visits</h2>
        <p>Would you like Milo and Jessa to bring<br>Pimble and Wocket to your school?<br>Learn more <a href="#">here...</a></p>
      </div>
    </div>
    <div class="half-right">
      <div class="readers">
        <h2>From out Readers</h2>
        <blockquote>Lorem Ipsum is simply dummy text of the printing and typesetting industry. Lorem Ipsum has been the industry's standard dummy text ever since when an unknown printer took a book.</blockquote>
        <cite>- Amanda</cite>
        <blockquote>Lorem Ipsum is simply dummy text of the printing and typesetting industry. Lorem Ipsum has been the industry's standard dummy text ever since when an unknown printer took a book.</blockquote>
        <cite>- Oliver</cite>
      </div>
    </div>
  </section>

  <div class="art art-feather" role="img" aria-label="Eagle feather illustration"></div>

  <footer class="site-footer">Copyright © 2014, Pimble Wocket Enterprises</footer>
</body>
</html>
```